Webdesign für Immobilienmanagement
Zielgruppe
Immobilienmanagement Unternehmen / allg. Hausverwaltung , Hausmeisterservice, Grünanlagenpflege, Unterhaltsreinigung, Winterdienst
Zielgruppe: Mieter und Wohnungseigentümer
Aufgabenstellung
Farben: weiß/grün
keine Kopie der alten Seite
nutzerfreundliche Unternehmenswebseite
Logo vorhanden auf alter Webseite

```html
<!DOCTYPE html>
<html lang="de">
<head>
<meta charset="utf-8">
<title>HAVENO Immobilien-Management</title>
<link rel="stylesheet" href="https://fonts.googleapis.com/css2?family=Hind:wght@400;500;600;700&display=swap">
<style>
:root{
  --green:#52ab37;
  --green-dark:#3f8f2a;
  --text:#6b6b6b;
  --nav:#777777;
  --white:#ffffff;
  --photo-sky:#6fa8dc;
  --photo-grass:#5fae3a;
  --photo-room:#e9e4dc;
  --photo-box:#c79a66;
}
*{margin:0;padding:0;box-sizing:border-box}
html,body{width:817px;height:1200px;overflow:hidden;background:var(--white)}
body{position:relative;font-family:"Hind",sans-serif;color:var(--text)}
.abs{position:absolute}
.brand{left:14px;top:11px;width:132px;height:44px;background:#f4f4f4;display:flex;align-items:center;gap:8px;padding-left:6px}
.brand-name{font-weight:700;font-size:20px;color:var(--green);line-height:1}
.brand-square{width:20px;height:20px;background:#8a8a8a}
.nav{top:21px;font-size:8.5px;color:var(--nav);line-height:12px}
.nav.active{color:var(--green)}
.hero-photo{left:276px;top:69px;width:513px;height:343px;border-radius:70px 90px 60px 40px / 70px 90px 80px 40px;background:linear-gradient(180deg,var(--photo-sky) 0%,#b9d3ea 38%,#cfcac2 52%,var(--photo-grass) 70%,#4c9a2c 100%)}
.hero-card{left:0;top:98px;width:330px;height:171px;background:var(--white);border-radius:0 34px 34px 0;box-shadow:0 3px 10px rgba(0,0,0,.08)}
.headline{left:0;width:330px;text-align:center;font-weight:700;font-size:38px;color:var(--green);line-height:40px}
.hero-sub{left:38px;top:226px;width:270px;font-size:8.5px;font-weight:600;line-height:11.5px}
.pill{left:16px;top:282px;width:232px;height:61px;background:var(--green);border-radius:30px;color:var(--white);font-weight:700;font-size:14.5px;line-height:20px;padding:10px 0 0 16px}
.services{left:43px;top:352px;list-style:none;font-size:11px;font-weight:600;line-height:15px}
.services li{display:flex;align-items:center;gap:5px}
.services li::before{content:"";width:6px;height:6px;border-radius:50%;background:var(--green)}
.family-photo{left:33px;top:476px;width:212px;height:319px;border-radius:44px;background:linear-gradient(180deg,#f2efe9 0%,var(--photo-room) 55%,var(--photo-box) 80%,#d9d4cc 100%)}
.intro{left:285px;top:429px;width:450px;font-size:8px;font-weight:600;line-height:11.5px}
.intro p{margin-bottom:11.5px}
.hours{left:285px;top:562px;font-size:11px;font-weight:600;color:var(--green);line-height:14px}
.hours p{margin-bottom:14px}
.note{left:285px;top:733px;width:270px;font-size:11px;font-weight:500;line-height:14px}
.note .mail{color:var(--green)}
.callback-title{left:578px;top:530px;font-size:10px;font-weight:700;color:var(--green)}
.callback{left:578px;top:556px;width:211px;height:249px;border:1.2px solid var(--green);border-radius:3px}
.field-label{left:613px;font-size:7px;font-weight:700;color:var(--green)}
.field{left:613px;width:141px;border:1px solid var(--green);border-radius:2px}
.send{left:613px;top:769px;width:55px;height:16px;border:1px solid var(--green);border-radius:2px;font-size:6.5px;font-weight:700;color:var(--green);text-align:center;line-height:16px}
.col-title{top:885px;font-size:10.5px;font-weight:700;color:var(--green)}
.col-text{font-size:11px;font-weight:500;line-height:15px}
.footer{left:0;top:1060px;width:817px;height:140px;background:var(--green)}
.footer-brand{left:130px;top:1085px;width:131px;height:44px;background:var(--white);display:flex;align-items:center;gap:8px;padding-left:8px}
.social{top:1164px;width:18px;height:18px;border-radius:50%;background:var(--white)}
.foot-title{top:1088px;font-size:7.5px;font-weight:700;color:var(--white)}
.foot-link{font-size:5.8px;color:var(--white);line-height:8px}
</style>
</head>
<body>

<div class="abs brand"><span class="brand-name">HAVENO</span><span class="brand-square"></span></div>
<span class="abs nav active" style="left:209px">Home</span>
<span class="abs nav" style="left:254px">über uns</span>
<span class="abs nav" style="left:312px">Hausverwaltung</span>
<span class="abs nav" style="left:397px">Hausmeister</span>
<span class="abs nav" style="left:461px">Downloads</span>
<span class="abs nav" style="left:523px">Partnerlinks</span>
<span class="abs nav" style="left:588px">Kontakt</span>
<span class="abs nav" style="left:634px">Impressum</span>
<span class="abs nav" style="left:694px">Datenschutz</span>

<div class="abs hero-photo" role="img" aria-label="Foto eines modernen Einfamilienhauses mit großem Rasen unter blauem Himmel"></div>
<div class="abs hero-card"></div>
<div class="abs headline" style="top:118px">Lass uns finden</div>
<div class="abs headline" style="top:168px">Dein Traum..</div>
<p class="abs hero-sub">allg. Hausverwaltung , Hausmeisterservice, Grünanlagenpflege, Unterhaltsreinigung, Winterdienst</p>

<div class="abs pill">Ihr zuverlässiger Dienstleister<br>rund um die Immobilie</div>
<ul class="abs services">
  <li>Allgemeine Hausverwaltung</li>
  <li>Kaufmännische Betreuung</li>
  <li>Technische Betreuung</li>
  <li>Hausmeisterservice</li>
  <li>Grünanlagenpflege</li>
  <li>Unterhaltsreinigung</li>
  <li>Winterdienst</li>
</ul>

<div class="abs family-photo" role="img" aria-label="Foto einer Familie beim Einzug zwischen Umzugskartons in einer hellen Wohnung"></div>

<div class="abs intro">
  <p>&nbsp;auf der Homepage der HAVENO Immobilien-Management GmbH!</p>
  <p>Wir sind ein junges, freundliches, gut ausgebildetes Team, das sich mit all seiner Aufmerksamkeit und Kompetenz um Ihre Wünsche in Sachen Immobilien kümmert.<br>Möchten Sie eine Wohnung mieten, suchen Sie einen Hausmeister ... oder einen Verwalter für Ihre Immobilie?</p>
  <p>Schauen Sie sich unser Leistungsangebot an und überzeugen Sie sich selbst von den Vorteilen, die wir Ihnen bieten können.</p>
</div>

<div class="abs hours">
  <p>Unsere Geschäftszeiten:<br>Montag<br>09.00 - 12.00 Uhr</p>
  <p>Dienstag<br>09.00 - 12.00 Uhr und 13.00 - 15.00 Uhr</p>
  <p>Donnerstag<br>09.00 - 12.00 Uhr und 13.00 - 18.00 Uhr</p>
</div>

<div class="abs note">
  <p>&nbsp;Gesprächstermine außerhalb unserer Geschäftszeiten sind jederzeit nach vorheriger Vereinbarung möglich.</p>
  <p style="margin-top:14px;width:300px">Rufen Sie uns an oder schreiben Sie uns eine <span class="mail">E-Mail.</span></p>
</div>

<div class="abs callback-title">Rückrufservice</div>
<div class="abs callback"></div>
<span class="abs field-label" style="top:573px">Name</span>
<div class="abs field" style="top:589px;height:14px"></div>
<span class="abs field-label" style="top:611px">Email</span>
<div class="abs field" style="top:626px;height:15px"></div>
<span class="abs field-label" style="top:649px">Telefon</span>
<div class="abs field" style="top:664px;height:15px"></div>
<span class="abs field-label" style="top:687px">Message</span>
<div class="abs field" style="top:702px;height:58px"></div>
<div class="abs send">SEND</div>

<div class="abs col-title" style="left:95px">Wohnen und arbeiten ...</div>
<div class="abs col-text" style="left:95px;top:916px">zuverlässige Verwaltun</div>
<div class="abs col-text" style="left:95px;top:946px">günstige Konditionen</div>
<div class="abs col-text" style="left:95px;top:975px;width:180px">Erhalt und Verbesserung der Mietsache</div>
<div class="abs col-text" style="left:95px;top:1020px;width:180px">&nbsp;partnerschaftiche Beziehung zu den Mietern</div>

<div class="abs col-title" style="left:363px">Wir sind Mitglied ...</div>
<div class="abs col-text" style="left:363px;top:912px;width:140px">Verband der Hausverwalter Mittelland e.V.</div>

<div class="abs col-title" style="left:606px">Notdienst</div>
<div class="abs col-text" style="left:606px;top:912px;width:70px">Schnell &amp; kompetent</div>
<div class="abs col-text" style="left:606px;top:957px;width:140px">24 Std. am Tag und auch an den Wochenenden!</div>

<footer class="abs footer"></footer>
<div class="abs footer-brand"><span class="brand-name">HAVENO</span><span class="brand-square"></span></div>
<span class="abs social" style="left:139px"></span>
<span class="abs social" style="left:163px"></span>
<span class="abs social" style="left:186px"></span>
<span class="abs social" style="left:209px"></span>

<div class="abs foot-title" style="left:342px">Useful Links</div>
<span class="abs foot-link" style="left:342px;top:1112px">About</span>
<span class="abs foot-link" style="left:342px;top:1129px">Partners</span>
<span class="abs foot-link" style="left:342px;top:1147px">Contact</span>

<div class="abs foot-title" style="left:441px">Help?</div>
<span class="abs foot-link" style="left:441px;top:1112px">FAQ</span>
<span class="abs foot-link" style="left:441px;top:1129px">Term &amp; Conditi0on</span>
<span class="abs foot-link" style="left:441px;top:1147px">Policy</span>
<span class="abs foot-link" style="left:441px;top:1164px">Privacy</span>

<div class="abs foot-title" style="left:554px">Address</div>
<span class="abs foot-link" style="left:554px;top:1112px">HAVENO Immobilien-Management GmbH • Lindenweg 8 • 04100 Musterstadt</span>
<span class="abs foot-link" style="left:554px;top:1129px">Telefon: 0341/555-0 • Telefax: 0341/555-45 • Email: info@haveno-immobilien.de</span>

</body>
</html>
```